Vemtri Gymnastics Silver gym banner

We need a banner for our new gym.
It should have navy, light blue, lilac and purple colors with our name, logo and other wording in navy color. Colors should bleed one into the other.
File with name, logo and other wording is attached.
Words: Rhythmic gymnastics, ballet, etc should be on the bottom

Target Market(s)

Girls 3 to 16 years of age

Industry/Entity Type

Athletics

Font styles to use
Other font styles liked:
• Please use fonts on file included

Colors
0054AA
0677BA
7BADD7
CADEEF
E8F1F8
0094D4
00A9DD
6FCCEA
C7EBF8
E9F6FB
00AB8E
00BBA5
67D7C9
C6EFE9
E9F9F6
6B429C
8869AF
B7A5CE
E3DAEB
F3F0F8

Requirements
Must have
• our logo and name of the gym
Nice to have
• rhythmic gymnastics feel
Should not have
• bold colors

```html
<!DOCTYPE html>
<html lang="en">
<head>
<meta charset="utf-8">
<title>Vemtri Gymnastics Banner</title>
<link rel="stylesheet" href="https://fonts.googleapis.com/css2?family=Libre+Baskerville:wght@400;700&display=swap">
<style>
  :root {
    --navy: #26408f;
    --navy-deep: #1c3380;
    --royal: #2a3d8c;
    --purple: #8a6ad4;
    --lilac: #a997ea;
    --sky: #6fccf0;
    --sky-glow: #5cc4f4;
    --paper: #eff0f4;
    --divider: #a57ee0;
    --white: #ffffff;
  }
  html, body {
    margin: 0;
    padding: 0;
    width: 1200px;
    height: 851px;
    overflow: hidden;
    background: var(--paper);
  }
  .banner {
    position: relative;
    width: 1200px;
    height: 851px;
    overflow: hidden;
    font-family: "Libre Baskerville", Georgia, serif;
  }
  .banner-art {
    position: absolute;
    inset: 0;
    width: 1200px;
    height: 851px;
  }
  .brand-name {
    position: absolute;
    left: 110px;
    top: 172px;
    margin: 0;
    color: var(--white);
    font-weight: 700;
    font-size: 70px;
    line-height: 1;
    white-space: nowrap;
  }
  .brand-mark {
    position: absolute;
    left: 935px;
    top: 120px;
    width: 130px;
    height: 130px;
    border: 4px solid var(--white);
    border-radius: 50%;
    box-sizing: border-box;
  }
  .brand-tagline {
    position: absolute;
    right: 306px;
    top: 270px;
    margin: 0;
    color: var(--white);
    font-weight: 400;
    font-size: 28px;
    line-height: 1;
    white-space: nowrap;
  }
  .programs {
    position: absolute;
    left: 0;
    right: 0;
    top: 700px;
    margin: 0;
    padding: 0;
    list-style: none;
    text-align: center;
    color: var(--navy);
    font-weight: 700;
    font-size: 35px;
    line-height: 62px;
  }
  .programs .row { display: block; white-space: nowrap; }
  .programs .sep {
    display: inline-block;
    width: 4px;
    height: 42px;
    margin: 0 14px;
    background: var(--divider);
    vertical-align: -8px;
  }
</style>
</head>
<body>
<main class="banner">
  <svg class="banner-art" viewBox="0 0 1773 1166" preserveAspectRatio="none" aria-hidden="false">
    <defs>
      <linearGradient id="header-fill" x1="0" y1="0" x2="1" y2="0.25">
        <stop offset="0" stop-color="#1f3a86"/>
        <stop offset="0.45" stop-color="#2c3c8a"/>
        <stop offset="0.8" stop-color="#5a55b0"/>
        <stop offset="1" stop-color="#a07ae0"/>
      </linearGradient>
      <radialGradient id="corner-glow" cx="0" cy="0" r="0.35" gradientTransform="scale(1 1.5)">
        <stop offset="0" stop-color="var(--sky-glow)" stop-opacity="1"/>
        <stop offset="1" stop-color="#5cc4f4" stop-opacity="0"/>
      </radialGradient>
      <radialGradient id="corner-glow-right" cx="1" cy="0.9" r="0.3">
        <stop offset="0" stop-color="#b489f0" stop-opacity="0.9"/>
        <stop offset="1" stop-color="#b489f0" stop-opacity="0"/>
      </radialGradient>
      <linearGradient id="photo-warm" x1="0" y1="0" x2="1" y2="1">
        <stop offset="0" stop-color="#2a2224"/>
        <stop offset="0.55" stop-color="#b88a6e"/>
        <stop offset="1" stop-color="#1a1616"/>
      </linearGradient>
      <linearGradient id="photo-dark" x1="0" y1="0" x2="1" y2="1">
        <stop offset="0" stop-color="#1b1a1d"/>
        <stop offset="0.5" stop-color="#c99a82"/>
        <stop offset="1" stop-color="#141314"/>
      </linearGradient>
      <radialGradient id="ring-shadow">
        <stop offset="0" stop-color="#000" stop-opacity="0.35"/>
        <stop offset="1" stop-color="#000" stop-opacity="0"/>
      </radialGradient>
    </defs>

    <rect class="paper" width="1773" height="1166" fill="var(--paper)"/>

    <path class="header-field" d="M0,0 H1773 V640 C1500,760 1100,800 800,790 C500,780 250,720 0,590 Z" fill="url(#header-fill)"/>
    <path class="header-glow" d="M0,0 H1773 V640 C1500,760 1100,800 800,790 C500,780 250,720 0,590 Z" fill="url(#corner-glow)"/>
    <path class="header-glow-right" d="M0,0 H1773 V640 C1500,760 1100,800 800,790 C500,780 250,720 0,590 Z" fill="url(#corner-glow-right)"/>
    <path class="navy-sweep" d="M0,450 C220,570 480,650 800,690 L800,790 C500,780 250,720 0,590 Z" fill="var(--navy-deep)"/>

    <path class="lilac-band" d="M1476,675 C1600,620 1700,570 1773,500 V539 C1700,590 1600,640 1476,684 Z" fill="var(--lilac)"/>
    <path class="sky-band" d="M1476,684 C1600,640 1700,590 1773,539 V644 C1700,670 1600,700 1476,719 Z" fill="var(--sky)"/>

    <g class="photo-rings">
      <ellipse cx="436" cy="805" rx="110" ry="8" fill="url(#ring-shadow)"/>
      <ellipse cx="721" cy="905" rx="125" ry="9" fill="url(#ring-shadow)"/>
      <ellipse cx="1046" cy="905" rx="125" ry="9" fill="url(#ring-shadow)"/>
      <ellipse cx="1336" cy="805" rx="105" ry="8" fill="url(#ring-shadow)"/>

      <circle cx="436" cy="664" r="142" fill="var(--paper)"/>
      <circle cx="721" cy="729" r="164" fill="var(--paper)"/>
      <circle cx="1046" cy="729" r="164" fill="var(--paper)"/>
      <circle cx="1336" cy="664" r="138" fill="var(--paper)"/>

      <circle cx="436" cy="664" r="128" fill="url(#photo-dark)" role="img" aria-label="Photo: rhythmic gymnast in a sparkling leotard balancing a ball"/>
      <circle cx="721" cy="729" r="150" fill="url(#photo-dark)" role="img" aria-label="Photo: young gymnast leaping in a split with a pink ribbon"/>
      <circle cx="1046" cy="729" r="150" fill="url(#photo-warm)" role="img" aria-label="Photo: gymnast performing a back bend with leg raised"/>
      <circle cx="1336" cy="664" r="124" fill="url(#photo-dark)" role="img" aria-label="Photo: smiling girl in a green leotard holding a ball"/>
    </g>
  </svg>

  <h1 class="brand-name">Vemtri Gymnastics</h1>
  <div class="brand-mark"></div>
  <p class="brand-tagline">School of Champions</p>

  <ul class="programs">
    <li class="row">RHYTHMIC GYMNASTICS<span class="sep"></span>BALLROOM DANCE</li>
    <li class="row">BALLET<span class="sep"></span>STRETCHING<span class="sep"></span>HIP HOP</li>
  </ul>
</main>
</body>
</html>
```